Business Cards and label design needed!

I am a metalsmith, working in sterling silver, brass and moving slowly into adding some gold accent pieces. I also use patinas to add color to brass pieces. The peacock feather is used in my packaging, as both a label and tissue paper. I am attaching what I am currently using, and printing at home, but I need a design that I can have professionally printed. My website is www.fernhollowworks.com
Target Market(s)
Established Professionals, Independent thinkers, Art donors, Artist supporters
Industry/Entity Type
Jewelry
Contact Information for Business Card
I would like a business card with the basic contact information, including Facebook and Instagram. I currently use a peacock feather and would like to continue that. I like to use turquoise, Tiffany blue and colors in that direction. I am open to other suggestions. I would like to be able to transfer the design to oval labels as well.
Other font styles liked:
- Garamond or other fonts that have a slight script that is easy to read
Look and feel

```html
<!DOCTYPE html>
<html lang="en">
<head>
<meta charset="utf-8">
<title>Fern Hollow Works – Business Card</title>
<link href="https://fonts.googleapis.com/css2?family=Lato:wght@300;400&family=Pinyon+Script&display=swap" rel="stylesheet">
<style>
  :root {
    --backdrop: #0f1517;
    --card: #151515;
    --silver: #d6d6d6;
    --grey-text: #b9b9b9;
    --teal: #3fb6c9;
    --teal-deep: #1f8fb0;
  }
  html, body {
    margin: 0;
    padding: 0;
    width: 1200px;
    height: 800px;
    overflow: hidden;
    background: var(--backdrop);
    font-family: "Lato", sans-serif;
  }
  .canvas {
    position: relative;
    width: 1200px;
    height: 800px;
  }
  .card {
    position: absolute;
    top: 182px;
    width: 435px;
    height: 436px;
    border-radius: 36px;
    background: var(--card);
  }
  .card--front { left: 146px; }
  .card--back  { left: 620px; }

  .brand {
    position: absolute;
    display: flex;
    align-items: center;
    gap: 12px;
    color: var(--silver);
    font-weight: 300;
    white-space: nowrap;
  }
  .brand__dot {
    border-radius: 50%;
    background: var(--teal);
    flex: none;
  }
  .card--front .brand {
    left: 0; right: 0;
    top: 215px;
    justify-content: center;
    font-size: 38px;
  }
  .card--front .brand__dot { width: 18px; height: 18px; }

  .card--back .brand {
    right: 42px;
    top: 110px;
    font-size: 22px;
    gap: 8px;
  }
  .card--back .brand__dot { width: 11px; height: 11px; }

  .website {
    position: absolute;
    color: var(--teal);
    font-size: 19px;
    letter-spacing: 3.6px;
    white-space: nowrap;
  }
  .card--front .website {
    left: 0; right: 0;
    top: 350px;
    text-align: center;
  }
  .card--back .website {
    left: 34px;
    top: 372px;
  }

  .person-name {
    position: absolute;
    left: 34px;
    top: 214px;
    margin: 0;
    color: var(--silver);
    font-family: "Pinyon Script", cursive;
    font-weight: 400;
    font-size: 34px;
  }
  .contact {
    position: absolute;
    left: 34px;
    top: 292px;
    margin: 0;
    padding: 0;
    list-style: none;
    color: var(--grey-text);
    font-size: 17px;
  }
  .contact__item {
    display: flex;
    align-items: center;
    gap: 10px;
    height: 34px;
  }
  .contact__icon {
    width: 18px;
    height: 14px;
    fill: var(--teal);
    flex: none;
  }
</style>
</head>
<body>
<main class="canvas">
  <section class="card card--front">
    <div class="brand"><span class="brand__dot"></span>Fern Hollow Works</div>
    <div class="website">www.fernhollowworks.com</div>
  </section>

  <section class="card card--back">
    <div class="brand"><span class="brand__dot"></span>Fern Hollow Works</div>
    <h2 class="person-name">Marla Quinn</h2>
    <ul class="contact">
      <li class="contact__item">
        <svg class="contact__icon" viewBox="0 0 18 14" aria-hidden="true">
          <path d="M1 4 C1 1 17 1 17 4 L17 5.5 L13 5.5 L13 4 L5 4 L5 5.5 L1 5.5 Z"/>
          <path d="M5 6 L13 6 L16 13 L2 13 Z"/>
          <circle cx="9" cy="9.5" r="2" fill="#151515"/>
        </svg>
        555.014.2290
      </li>
      <li class="contact__item">
        <svg class="contact__icon" viewBox="0 0 18 14" aria-hidden="true">
          <rect x="0" y="1" width="18" height="12" rx="1"/>
          <path d="M1 2 L9 8.5 L17 2" fill="none" stroke="#151515" stroke-width="1.4"/>
        </svg>
        studio@fernhollowworks.com
      </li>
    </ul>
    <div class="website">www.fernhollowworks.com</div>
  </section>
</main>
</body>
</html>
```